Endocrinologist needs new stationery

I have a logo from MarkForge and now need stationery with the new logo.

Address: Suite 4, 282 Falcon Street, Richmond, VIC 3121
Phone: 03 9417 2253
Fax: 03 9417 2255
Website: www.drmaylacorwen.com.au
Email: admin@drmaylacorwen.com.au

```html
<!DOCTYPE html>
<html lang="en">
<head>
<meta charset="utf-8">
<title>Dr Mayla Corwen – Stationery</title>
<link href="https://fonts.googleapis.com/css2?family=Hind:wght@300;400;500;600&display=swap" rel="stylesheet">
<style>
  :root {
    --backdrop: #a9a8a9;
    --paper: #f5f2f3;
    --white: #ffffff;
    --brand-blue: #316c9c;
    --brand-blue-deep: #2a5d87;
    --brand-plum: #6b4560;
    --ink: #3c3c3c;
    --ink-soft: #555555;
  }
  * { box-sizing: border-box; margin: 0; padding: 0; }
  html, body { width: 1200px; height: 770px; overflow: hidden; }
  body {
    background: var(--backdrop);
    font-family: "Hind", sans-serif;
    color: var(--ink);
    position: relative;
  }
  .piece {
    position: absolute;
    background: var(--paper);
    box-shadow: 0 3px 8px rgba(0,0,0,0.28);
    overflow: hidden;
  }
  .wordmark {
    font-family: "Hind", sans-serif;
    font-weight: 300;
    color: var(--brand-blue);
    white-space: nowrap;
    letter-spacing: 0.5px;
  }
  .wave { position: absolute; left: 0; width: 100%; display: block; }
  .wave .band { fill: var(--brand-plum); }
  .wave .field { fill: var(--brand-blue); }

  /* business card front */
  .card-front { left: 86px; top: 46px; width: 218px; height: 125px; background: var(--brand-blue); }
  .card-front .wordmark {
    position: absolute; left: 0; right: 0; top: 48px; text-align: center;
    font-size: 21px; color: var(--brand-blue-deep);
  }

  /* business card back */
  .card-back { left: 337px; top: 46px; width: 218px; height: 125px; background: var(--white); }
  .card-back .wordmark { position: absolute; left: 0; right: 0; top: 22px; text-align: center; font-size: 21px; }
  .card-back .wave { top: 62px; height: 63px; }
  .card-back .contact {
    position: absolute; top: 91px; left: 0; right: 0;
    display: flex; justify-content: center; gap: 6px;
    color: var(--white); font-size: 5.4px; line-height: 6.6px;
  }
  .card-back .contact .address { text-align: right; padding-right: 6px; border-right: 0.6px solid rgba(255,255,255,0.8); }
  .contact-row { display: flex; align-items: center; gap: 3px; }
  .icon { flex: none; }

  /* envelope front */
  .envelope-front { left: 61px; top: 203px; width: 562px; height: 255px; }
  .envelope-front .wordmark { position: absolute; left: 32px; top: 24px; font-size: 22px; }
  .envelope-front .return-address { position: absolute; left: 32px; top: 62px; font-size: 7.6px; color: var(--ink-soft); letter-spacing: 0.3px; }
  .envelope-front .wave { bottom: 0; height: 40px; }

  /* envelope back */
  .envelope-back { left: 57px; top: 480px; width: 559px; height: 253px; }
  .envelope-back .flap { position: absolute; left: 0; top: 0; width: 559px; height: 94px; }
  .envelope-back .flap path { fill: var(--brand-blue); }
  .envelope-back .wordmark {
    position: absolute; left: 0; right: 0; top: 32px; text-align: center;
    font-size: 21px; color: var(--white);
  }

  /* letterhead */
  .letterhead { left: 643px; top: 33px; width: 496px; height: 700px; }
  .letterhead .wordmark { position: absolute; left: 44px; top: 50px; font-size: 22px; }
  .letterhead .header-address {
    position: absolute; right: 155px; top: 47px; text-align: right;
    font-size: 7.6px; line-height: 9.2px; color: var(--ink-soft); font-weight: 400;
    padding-right: 7px; border-right: 0.7px solid var(--ink-soft);
  }
  .letterhead .header-contact {
    position: absolute; left: 352px; top: 44px;
    font-size: 7.6px; line-height: 9.2px; color: var(--ink-soft);
  }
  .letterhead .header-contact .contact-row { gap: 4px; }
  .letterhead .header-contact .icon { fill: var(--brand-blue); }
  .letter-date { position: absolute; left: 48px; top: 177px; font-size: 9.4px; font-weight: 500; }
  .letter-recipient { position: absolute; left: 48px; top: 213px; font-size: 9.2px; line-height: 12px; font-weight: 500; }
  .letter-body { position: absolute; left: 47px; top: 284px; width: 401px; font-size: 7.8px; line-height: 12px; text-align: justify; color: var(--ink-soft); }
  .letter-body p + p { margin-top: 12px; }
  .signature { position: absolute; left: 356px; top: 526px; width: 80px; height: 42px; background: linear-gradient(90deg, rgba(40,40,40,0.12), rgba(40,40,40,0.05)); }
  .signer-title { position: absolute; left: 377px; top: 560px; font-size: 8px; color: var(--ink-soft); }
  .letterhead .wave { bottom: 0; height: 40px; }
</style>
</head>
<body>

  <section class="piece card-front">
    <div class="wordmark">Dr Mayla Corwen</div>
  </section>

  <section class="piece card-back">
    <div class="wordmark">Dr Mayla Corwen</div>
    <svg class="wave" viewBox="0 0 1000 120" preserveAspectRatio="none" aria-hidden="true">
      <path class="band" d="M0,0 C300,40 700,42 1000,10 L1000,14 C700,50 300,48 0,10 Z"/>
      <path class="field" d="M0,16 C300,56 700,58 1000,18 L1000,120 L0,120 Z"/>
    </svg>
    <div class="contact">
      <div class="address">Suite 4, 282 Falcon Street<br>Richmond, VIC 3121<br>www.drmaylacorwen.com.au</div>
      <div class="details">
        <div class="contact-row"><svg class="icon" width="5" height="5" viewBox="0 0 10 10"><path fill="#fff" d="M2,0 L4,2.5 L3,4 Q4.5,6 6,7 L7.5,6 L10,8 L8.5,10 Q3,9 0,1.5 Z"/></svg>03 9417 2253</div>
        <div class="contact-row"><svg class="icon" width="5" height="5" viewBox="0 0 10 10"><path fill="#fff" d="M2,0 H8 V3 H10 V8 H0 V3 H2 Z M1,9 H9 V10 H1 Z"/></svg>03 9417 2255</div>
        <div class="contact-row"><svg class="icon" width="5" height="5" viewBox="0 0 10 10"><path fill="#fff" d="M0,2 H10 V8 H0 Z"/><path fill="none" stroke="#316c9c" stroke-width="1" d="M0,2 L5,5.5 L10,2"/></svg>admin@drmaylacorwen.com.au</div>
      </div>
    </div>
  </section>

  <section class="piece envelope-front">
    <div class="wordmark">Dr Mayla Corwen</div>
    <div class="return-address">Suite 4, 282 Falcon Street, Richmond, VIC 3121</div>
    <svg class="wave" viewBox="0 0 1000 120" preserveAspectRatio="none" aria-hidden="true">
      <path class="band" d="M0,0 C300,80 700,88 1000,10 L1000,14 C700,96 300,92 0,22 Z"/>
      <path class="field" d="M0,40 C300,104 700,106 1000,26 L1000,120 L0,120 Z"/>
    </svg>
  </section>

  <section class="piece envelope-back">
    <svg class="flap" viewBox="0 0 559 94" aria-hidden="true">
      <path d="M0,0 H559 L546,60 Q540,93 505,93 H54 Q19,93 13,60 Z"/>
    </svg>
    <div class="wordmark">Dr Mayla Corwen</div>
  </section>

  <section class="piece letterhead">
    <div class="wordmark">Dr Mayla Corwen</div>
    <div class="header-address">Suite 4<br>282 Falcon Street<br>Richmond, VIC 3121</div>
    <div class="header-contact">
      <div class="contact-row"><svg class="icon" width="6" height="6" viewBox="0 0 10 10"><path d="M2,0 L4,2.5 L3,4 Q4.5,6 6,7 L7.5,6 L10,8 L8.5,10 Q3,9 0,1.5 Z"/></svg>03 9417 2253</div>
      <div class="contact-row"><svg class="icon" width="6" height="6" viewBox="0 0 10 10"><path d="M2,0 H8 V3 H10 V8 H0 V3 H2 Z M1,9 H9 V10 H1 Z"/></svg>03 9417 2255</div>
      <div class="contact-row"><svg class="icon" width="6" height="6" viewBox="0 0 10 10"><path d="M0,2 H10 V8 H0 Z"/><path fill="none" stroke="#f5f2f3" stroke-width="1" d="M0,2 L5,5.5 L10,2"/></svg>admin@drmaylacorwen.com.au</div>
      <div class="contact-row"><svg class="icon" width="6" height="6" viewBox="0 0 10 10"><circle cx="5" cy="5" r="5"/></svg>www.drmaylacorwen.com.au</div>
    </div>

    <div class="letter-date">Cartagena de Indias, Ocober 12,2015</div>
    <div class="letter-recipient">Sr.<br>TOMAS IBARRA<br>Web Master<br>City</div>

    <div class="letter-body">
      <p>Contrary to popular belief, Lorem Ipsum is not simply random text. It has roots in a piece of classical Latin literature from 45 BC, making it over 2000 years old. Daniel Ashford, a Latin professor at Westbrook College in Virginia, looked up one of the more obscure Latin words, consectetur, from a Lorem Ipsum passage, and going through the cites of the word in classical literature,</p>
      <p>discovered the undoubtable source. Lorem Ipsum comes from sections 1.10.32 and 1.10.33 of "de Finibus Bonorum et Malorum" (The Extremes of Good and Evil) by Quintus Arrel, written in 45 BC. This book is a treatise on the theory of ethics, very popular during the Renaissance. The first line of Lorem Ipsum, "Lorem ipsum dolor sit amet..", comes from a line in section 1.10.32.</p>
      <p>The standard chunk of Lorem Ipsum used since the 1500s is reproduced below for those interested. Sections 1.10.32 and 1.10.33 from "de Finibus Bonorum et Malorum" by Quintus Arrel are also reproduced in their exact original form, accompanied by English versions from the 1914 translation by H. Lindqvist.</p>
      <p>There are many variations of passages of Lorem Ipsum available, but the majority have suffered alteration in some form, by injected humour, or randomised words which don't look even slightly believable. If you are going to use a passage of Lorem Ipsum, you need to be sure there isn't anything embarrassing hidden in the middle of text. All the Lorem Ipsum generators o</p>
    </div>

    <div class="signature" role="img" aria-label="Handwritten signature of Evan Marsh"></div>
    <div class="signer-title">CEO/ FOUNDER</div>

    <svg class="wave" viewBox="0 0 1000 120" preserveAspectRatio="none" aria-hidden="true">
      <path class="band" d="M0,0 C300,80 700,88 1000,8 L1000,12 C700,96 300,92 0,24 Z"/>
      <path class="field" d="M0,42 C300,104 700,106 1000,24 L1000,120 L0,120 Z"/>
    </svg>
  </section>

</body>
</html>
```